A brand new wordpress website for my business which will replace my current site www.harbornetcall.com.au, As i rank quite well in google will it be ok to keep my current URL's. I sell the following service and products

1. Voip Provider (Main service) we sell directly the the end user but also we would like to get resellers and agents to sell our services. agents selling our brand resellers sell our services branded as theirs
2. Hosted Pbx (main service) home page must push this service explaining the benifits and features that come with a hosted pbx, we also have business plans based on number of extensions (phones) the customer requires
3. Tornax IP Pbx (product) only selling IP Pbx and selected software
4. Velbox IP Pbx (product)
5. Quorvin IP Phones (this is the main VoIP phone we sell)
6. lumora phones (to be on a landing page only not apart of the main site)
7. selected headsets from Dravensonic (products)
8. Meridal Conference phone (VoIP model only)
9. we can supply fax to email service

we would like a support page with user guides (step by step instructions on our products and services and FAQ's about all products and services

we have a carrier grade softswitch (telco billing system) z7ledger http://www.pinwheelledger.org this system has a ticketing system, customer and agent login I would like a URL link from our website so customers can login to this system. also it is possible to skin z7ledger to look like our website

VoIP business plans

$0 per month
call rate .12c land line calls
.24c per minute mobile calls

$25 per month
250 Free local land line calls
call rate is .10c land line calls .22c per minute mobile calls

$50 per month
500 Free local land line calls
call rate .09 land line calls .20c per minute mobile calls

$100 per month
1000 free local land line calls
call rate .08c land line calls .18c per minute mobile calls

all mobile calls are billed per second no flag fall

also require a link to international call rates

We can port your existing telephone number from any carrier or supply new Australian telephone numbers

02, 03, 07, 08, 131, 1300, 1800

Designs i like www.tralcom.com.au and www.orbitelphone.com

I would like the website to be white and bright

Reason: Please use images of the products I sell only

Target Market(s)

business customers only

Industry/Entity Type

Requirements
Must have
• all pages must have its own banner to reflect the product or service we are selling. the home page can automatically change to show all pages with a link straight to the page in question

for example if on the home page the banner for quorvin phone is displaying if someone click on the banner they will be redirected to the quorvin page

Must Be SEO friendly
Nice to have
• shopping cart via paypal for all products but before customer checks out i would like to offer two options

1. Pre configure the item and ship to your address for existing customers
2. would you like a harbor net call technician to attend your office and install the item in person (costs involved $60 call out fee $120 per hours every item sold charge .50 hour and only the one call out fee)

new and existing customers can book service work via the website
1. describe the work required (maybe we need to give a few option)
2. company details
3. pre payment (checkout via paypal) can we put the paypal fees back on to the customer?

```html
<!DOCTYPE html>
<html lang="en">
<head>
<meta charset="utf-8">
<title>Harbor Net Call – Business Phone Systems &amp; Hosted PBX</title>
<link rel="stylesheet" href="https://fonts.googleapis.com/css2?family=Arimo:wght@400;700&family=Oswald:wght@300;400&display=swap">
<style>
:root{
  --blue:#0a63a8;
  --orange:#f15a22;
  --caption:#5b5b5b;
  --dot:#9b9b9b;
  --footer-bg:#222222;
  --footer-text:#b5b5b5;
  --green:#6bb62e;
  --card-border:#a9a9a9;
}
*{box-sizing:border-box;margin:0;padding:0}
html,body{width:1200px;height:1175px;overflow:hidden;background:#fff}
body{font-family:"Arimo",Arial,sans-serif}
.page{position:relative;width:1200px;height:1175px;overflow:hidden}
.header{position:absolute;left:0;top:0;width:1200px;height:424px;
  background:linear-gradient(180deg,#f7f8fa 0%,#f4f6f8 88%,#e6e6e6 100%)}
.top-line{position:absolute;left:0;top:0;width:1200px;height:8px;background:var(--blue)}
.phone-tab{position:absolute;left:740px;top:0}
.phone-number{position:absolute;left:830px;top:8px;color:#fff;font-size:18px;display:flex;align-items:center;gap:8px}
.brand{position:absolute;left:170px;top:40px;display:flex;align-items:center;gap:10px;
  font-weight:700;font-size:34px;color:var(--blue)}
.brand-dot{width:18px;height:18px;border-radius:50%;background:var(--blue)}
.hero-visual{position:absolute;left:195px;top:150px;width:320px;height:185px;border-radius:50% 50% 30% 30%;
  background:radial-gradient(ellipse at 50% 45%,#4a4d52 0%,#2b2d31 55%,#dfe6ee 75%,rgba(240,244,248,0) 100%)}
.hero-caption{position:absolute;left:150px;top:343px;width:450px;height:32px;background:var(--caption);
  color:#fff;font-size:18px;text-align:center;line-height:32px}
.slider-dots{position:absolute;left:258px;top:385px;display:flex;gap:6px}
.slider-dots span{width:19px;height:19px;border-radius:50%;background:var(--dot)}
.slider-dots .active{background:var(--blue)}
.welcome{position:absolute;right:152px;top:164px;text-align:right;font-family:"Oswald",sans-serif;font-weight:300;color:var(--blue)}
.welcome h1{font-weight:300;font-size:38px;line-height:46px;letter-spacing:-.3px}
.welcome p{font-size:19px;line-height:36px;margin-top:2px}
.more-btn{position:absolute;left:908px;top:291px;width:141px;height:35px;border:1px solid #b8bdb5;
  background:linear-gradient(180deg,#f3f5f1 0%,#d7ddd3 60%,#c5ccc0 100%);
  font-family:"Oswald",sans-serif;font-weight:300;font-size:19px;color:var(--blue);text-align:center;line-height:33px}
.main-nav{position:absolute;right:151px;top:384px;font-size:14.5px;color:var(--blue)}
.main-nav a{color:var(--blue);text-decoration:none}
.main-nav .current{color:var(--green)}
.main-nav .sep{margin:0 6px}
.orange-band{position:absolute;left:0;top:424px;width:1200px;height:18px;background:var(--orange)}
.login-tab{position:absolute;left:750px;top:441px}
.login-label{position:absolute;left:862px;top:439px;color:#fff;font-size:23px}
.side-frame{position:absolute;top:470px}
.arrow{position:absolute;top:664px}
.card{position:absolute;top:532px;width:190px;height:375px;border:1px solid var(--card-border);
  background:linear-gradient(180deg,#fff 0%,#fff 85%,#f0f0f0 100%)}
.card-photo{position:absolute;left:11px;top:68px;width:168px;height:168px;border-radius:50%;border:5px solid #b4b4b4}
.card-label{position:absolute;top:261px;height:28px;color:#fff;font-size:18px;text-align:center;line-height:28px}
.footer-rule{position:absolute;left:0;top:950px;width:1200px;height:3px;border-top:1px solid #9a9a9a;border-bottom:1px solid #cfcfcf}
.footer{position:absolute;left:0;top:955px;width:1200px;height:220px;background:var(--footer-bg);
  color:var(--footer-text);font-size:14px;text-align:center}
.footer p{position:absolute;left:30px;width:1200px}
.footer a{color:var(--footer-text);text-decoration:none}
.footer .current{color:#2c6fb0}
</style>
</head>
<body>
<div class="page">
  <header class="header">
    <div class="top-line"></div>
    <svg class="phone-tab" width="310" height="42" viewBox="0 0 310 42">
      <path d="M0 0 H310 C285 8 270 40 230 40 H90 C50 40 30 8 0 0 Z" fill="var(--blue)"/>
    </svg>
    <div class="phone-number">
      <svg width="12" height="18" viewBox="0 0 12 18"><path d="M4 1 C1 2 0 5 1 9 C2 13 5 17 9 17 L11 15 L8 11 L6 12 C5 10 4 8 4 6 L6 5 L5 1 Z" fill="#fff"/></svg>
      1300 555 019
    </div>
    <div class="brand"><span class="brand-dot"></span>Harbor Net Call</div>
    <div class="hero-visual" role="img" aria-label="Meridal conference phone product photo"></div>
    <div class="hero-caption">Meridal400c-318</div>
    <div class="slider-dots"><span class="active"></span><span></span><span></span><span></span><span></span><span></span><span></span></div>
    <div class="welcome">
      <h1>Welcome to harbornetcall</h1>
      <p>Small to Medium Business Phone Systems &amp;<br>Hosted PBX Solutions</p>
    </div>
    <a class="more-btn">More</a>
    <nav class="main-nav">
      <a class="current">Home</a><span class="sep">|</span><a>About Us</a><span class="sep">|</span><a>Contact Us</a><span class="sep">|</span><a>Hosted PBX</a><span class="sep">&nbsp;|</span><a>Sign Up</a>
    </nav>
  </header>

  <div class="orange-band"></div>
  <svg class="login-tab" width="300" height="36" viewBox="0 0 300 36">
    <path d="M0 0 H300 C270 6 255 34 220 34 H80 C45 34 30 6 0 0 Z" fill="var(--orange)"/>
  </svg>
  <div class="login-label">Login</div>

  <svg class="side-frame" style="left:152px" width="45" height="450" viewBox="0 0 45 450">
    <path d="M5 10 C30 60 40 80 40 120 V370 C40 400 20 420 2 440" fill="none" stroke="#e2e2e2" stroke-width="10"/>
    <path d="M14 60 C34 80 38 95 38 120 V370 C38 390 30 400 16 410" fill="none" stroke="#8e8e8e" stroke-width="3"/>
  </svg>
  <svg class="side-frame" style="left:1005px" width="45" height="450" viewBox="0 0 45 450">
    <path d="M40 10 C15 60 5 80 5 120 V370 C5 400 25 420 43 440" fill="none" stroke="#e2e2e2" stroke-width="10"/>
    <path d="M31 60 C11 80 7 95 7 120 V370 C7 390 15 400 29 410" fill="none" stroke="#8e8e8e" stroke-width="3"/>
  </svg>
  <svg class="arrow" style="left:160px" width="26" height="86" viewBox="0 0 26 86"><path d="M2 2 L23 43 L2 84" fill="none" stroke="#5a5a5a" stroke-width="5"/></svg>
  <svg class="arrow" style="left:1015px" width="26" height="86" viewBox="0 0 26 86"><path d="M24 2 L3 43 L24 84" fill="none" stroke="#5a5a5a" stroke-width="5"/></svg>

  <section class="card" style="left:205px">
    <div class="card-photo" role="img" aria-label="Quorvin IP desk phone" style="background:radial-gradient(circle,#3a3c40 0%,#6b6e73 45%,#f2f2f2 70%)"></div>
    <div class="card-label" style="left:19px;width:152px;background:var(--blue)">Our Products</div>
  </section>
  <section class="card" style="left:404px">
    <div class="card-photo" role="img" aria-label="Customer service staff on the phone" style="background:linear-gradient(135deg,#cfd8e3 0%,#8a95a5 50%,#e8d6c8 100%)"></div>
    <div class="card-label" style="left:13px;width:152px;background:var(--orange);top:263px">Our Service</div>
  </section>
  <section class="card" style="left:602px">
    <div class="card-photo" role="img" aria-label="Stacked columns representing plan pricing" style="background:linear-gradient(180deg,#f4f4f4 0%,#d6d6d2 55%,#b9b8b2 100%)"></div>
    <div class="card-label" style="left:8px;width:174px;background:var(--orange);top:263px">VoIP Plans</div>
  </section>
  <section class="card" style="left:800px">
    <div class="card-photo" role="img" aria-label="Paid stamp representing billing" style="background:linear-gradient(160deg,#5b5fc0 0%,#9a9ab0 40%,#e6e8ee 100%)"></div>
    <div class="card-label" style="left:21px;width:152px;background:var(--orange);top:263px">Z7 Ledger</div>
  </section>

  <div class="footer-rule"></div>
  <footer class="footer">
    <p style="top:70px"><a class="current">Home</a> | <a>About</a> | <a>Hosted PBX</a> | <a>Contact Us</a> | <a>Telephone Systems</a> | <a>Plans &amp; Signup</a> | <a>Terms And Privacy</a> | <a>Returns Policy</a> | <a>Sitemap</a></p>
    <p style="top:104px"><a>Phone Systems Sydney</a> | <a>Hosted PBX</a> | <a>VoIP Providers</a> | <a>VoIP Providers Sydney</a></p>
    <p style="top:138px">Copyright 2013 Harbor Net Call</p>
  </footer>
</div>
</body>
</html>
```